Makeup Artist looking to redesign business card

I'm a makeup artist relocating from Sydney to the Tweed Heads Area. I will be providing makeup services (primarily in bridal/wedding, events) in the Tweed Heads, Gold Coast and Byron Bay areas. I have attached 2 photos to use on the front OR back of the card. I can't decide which photo will work best, so I have provided both for you to decide. I'm open to the idea of a logo creation, or just the business name. Business name is;
Harriet Rose Calloway Makeup Artist
or
Harriet Calloway Makeup Artist
I will need a space for ABN, mobile number, email address and website address.
I'm open to the photo being either colour or B&W.
Font and background colour could be B&W or another colour, again I'm looking for something different and creative, which is why I'm posting this ad.
I do like the idea of the photo being panoramic, so the veil material continues off to the side.
I'm excited to see what people come up with!!!
Target Market(s)
ladies
Industry/Entity Type
Business
Contact Information for Business Card
or

```html
<!DOCTYPE html>
<html lang="en">
<head>
<meta charset="utf-8">
<title>Harriet Calloway Makeup Artist – Business Card</title>
<link rel="stylesheet" href="https://fonts.googleapis.com/css2?family=Questrial&family=Montserrat:wght@700&display=swap">
<style>
  :root {
    --page: #e9e6e3;
    --card-dark: #141414;
    --card-dark-edge: #1f1f1f;
    --card-light: #f4f4f4;
    --card-light-shade: #dedede;
    --magenta: #d43fc4;
    --magenta-deep: #b0239f;
    --white: #ffffff;
    --photo-skin: #e8c9b4;
    --photo-veil: #ececec;
  }
  * { box-sizing: border-box; margin: 0; padding: 0; }
  html, body { width: 1200px; height: 780px; overflow: hidden; }
  body {
    background: var(--page);
    font-family: "Questrial", sans-serif;
    display: flex;
    align-items: center;
    justify-content: center;
    gap: 40px;
  }
  .card {
    width: 560px;
    height: 320px;
    border-radius: 22px;
    position: relative;
    overflow: hidden;
    box-shadow: 0 10px 26px rgba(0,0,0,0.22);
  }

  /* Dark side */
  .card--back {
    background: linear-gradient(160deg, var(--card-dark-edge), var(--card-dark));
    color: var(--white);
  }
  .card--back .brand {
    position: absolute;
    left: 0; top: 0;
    width: 270px; height: 100%;
    display: flex;
    flex-direction: column;
    align-items: center;
    justify-content: center;
    gap: 10px;
    color: var(--magenta);
    font-size: 23px;
    line-height: 1.15;
    text-align: center;
  }
  .brand__dot {
    width: 12px; height: 12px;
    border-radius: 50%;
    background: var(--magenta);
  }
  .card--back .divider {
    position: absolute;
    left: 278px; top: 40px;
    width: 1px; height: 240px;
    background: linear-gradient(to bottom, transparent, var(--magenta-deep), transparent);
  }
  .card--back .details {
    position: absolute;
    left: 312px; top: 62px;
    right: 20px;
  }
  .details__name {
    font-family: "Montserrat", sans-serif;
    font-weight: 700;
    font-size: 22px;
    color: var(--magenta);
    letter-spacing: -0.3px;
  }
  .details__role {
    font-size: 16px;
    margin-bottom: 30px;
  }
  .contact-list { list-style: none; }
  .contact-list li {
    display: flex;
    align-items: center;
    gap: 8px;
    font-size: 14.5px;
    margin-bottom: 7px;
    white-space: nowrap;
  }
  .contact-icon {
    width: 17px; height: 17px;
    background: var(--magenta);
    border-radius: 3px;
    display: flex; align-items: center; justify-content: center;
    flex-shrink: 0;
  }
  .contact-abn { font-size: 14.5px; margin-top: 10px; }
  .contact-abn span { color: var(--magenta); }

  /* Light side */
  .card--front {
    background: radial-gradient(ellipse at 40% 30%, var(--white), var(--card-light) 45%, var(--card-light-shade));
  }
  .card--front .brand {
    position: absolute;
    left: 40px; top: 46px;
    width: 270px;
    display: flex;
    flex-direction: column;
    align-items: center;
    gap: 10px;
    color: var(--magenta);
    font-size: 23px;
    line-height: 1.15;
    text-align: center;
  }
  .card--front .website {
    position: absolute;
    left: 34px; bottom: 34px;
    color: var(--magenta);
    font-size: 15px;
  }
  .card--front .portrait {
    position: absolute;
    right: 0; top: 0;
    width: 300px; height: 100%;
    background:
      radial-gradient(ellipse at 68% 45%, var(--photo-skin) 0 28%, transparent 45%),
      linear-gradient(to right, transparent, var(--photo-veil) 35%);
  }
</style>
</head>
<body>

  <section class="card card--back">
    <div class="brand">
      <div class="brand__dot"></div>
      <div>Harriet Rose Calloway<br>Makeup Artist</div>
    </div>
    <div class="divider"></div>
    <div class="details">
      <div class="details__name">Harriet Calloway</div>
      <div class="details__role">Makeup Artist</div>
      <ul class="contact-list">
        <li>
          <span class="contact-icon">
            <svg width="11" height="11" viewBox="0 0 24 24"><path fill="#141414" d="M6.6 10.8a15.1 15.1 0 0 0 6.6 6.6l2.2-2.2a1 1 0 0 1 1-.25 11.4 11.4 0 0 0 3.6.57 1 1 0 0 1 1 1V20a1 1 0 0 1-1 1A17 17 0 0 1 3 4a1 1 0 0 1 1-1h3.5a1 1 0 0 1 1 1c0 1.25.2 2.45.57 3.57a1 1 0 0 1-.25 1z"/></svg>
          </span>0412-555-038
        </li>
        <li>
          <span class="contact-icon">
            <svg width="11" height="11" viewBox="0 0 24 24"><rect x="2" y="5" width="20" height="14" fill="none" stroke="#141414" stroke-width="2.4"/><path d="M2 5l10 8 10-8" fill="none" stroke="#141414" stroke-width="2.4"/></svg>
          </span>hello@harrietcalloway.com
        </li>
        <li>
          <span class="contact-icon">
            <svg width="11" height="11" viewBox="0 0 24 24"><g fill="none" stroke="#141414" stroke-width="2.2"><circle cx="12" cy="12" r="9"/><ellipse cx="12" cy="12" rx="4" ry="9"/><path d="M3 12h18"/></g></svg>
          </span>www.harrietcalloway.com
        </li>
      </ul>
      <div class="contact-abn"><span>ABN:</span> 4820391756</div>
    </div>
  </section>

  <section class="card card--front">
    <div class="brand">
      <div class="brand__dot"></div>
      <div>Harriet Rose Calloway<br>Makeup Artist</div>
    </div>
    <div class="website">www.harrietcalloway.com</div>
    <div class="portrait" role="img" aria-label="Portrait photo of the makeup artist in a white off-shoulder top, fading into the light card background"></div>
  </section>

</body>
</html>
```